Business Card Design

Marla Quibbet
Artist of Contemporary/Modern/Representational Art
Contact: 0457219308
Please include my web site (thanks)! http://www.artvault913.com.au/marla-quibbet
And
Email: marlaquibbet@fernpost.example

Target Market(s)

Modern professional People who know what they like in modern contemporary art and have the means to purchase it.

Industry/Entity Type

Business

Contact Information for Business Card

Marla Quibbet
Contact: 0457219308

Font styles to use
Sans Serif

Requirements
Must have
• Simplicity & to the point
Keep the font modern/ contemporary
Nice to have
• A portrait of me and one piece of work on the business card (one on each side).
Should not have
• I'm not into butterflies.
No feminine style swirls
Nor I like swirls that look like tatoos

```html
<!DOCTYPE html>
<html lang="en">
<head>
<meta charset="utf-8">
<title>Marla Quibbet — Business Card</title>
<link rel="stylesheet" href="https://fonts.googleapis.com/css2?family=Arimo:wght@400;700&display=swap">
<style>
  :root {
    --stage: #000000;
    --card: #2c302e;
    --card-edge: #262a28;
    --olive: #c6c15f;
    --olive-text: #c9c35a;
    --ink-light: #f4f4f2;
    --icon: #b9b58a;
    --frame-line: #cfd8b0;
  }
  * { margin: 0; padding: 0; box-sizing: border-box; }
  html, body { width: 1200px; height: 900px; overflow: hidden; background: var(--stage); }
  body { position: relative; font-family: "Arimo", Helvetica, Arial, sans-serif; }

  .card { position: absolute; width: 490px; height: 300px; overflow: hidden; }

  /* front */
  .card-front {
    left: 5px; top: 133px;
    background: radial-gradient(ellipse at 40% 40%, #323634 0%, var(--card) 60%, var(--card-edge) 100%);
  }
  .portrait {
    position: absolute; left: 60px; top: 45px; width: 87px; height: 107px;
    border: 2px solid var(--olive);
    background: linear-gradient(160deg, #6f8a6a 0%, #8a6a5a 45%, #d86a3a 80%, #c9402c 100%);
  }
  .accent-block {
    position: absolute; left: 60px; top: 159px; width: 87px; height: 141px;
    background: var(--olive);
  }
  .identity { position: absolute; left: 186px; top: 106px; }
  .name { color: var(--ink-light); font-weight: 700; font-size: 13.5px; line-height: 18px; }
  .role { color: var(--olive-text); font-size: 14px; line-height: 18px; font-weight: 400; }
  .contacts { position: absolute; left: 187px; top: 200px; list-style: none; }
  .contacts li {
    display: flex; align-items: center; gap: 9px;
    color: var(--ink-light); font-size: 13px; line-height: 17.5px;
  }
  .contacts svg { width: 10px; height: 10px; flex: none; stroke: var(--icon); fill: none; stroke-width: 1.1; }

  /* back */
  .card-back { left: 5px; top: 495px; height: 303px; background: var(--card); display: flex; gap: 3px; padding: 2px; }
  .artwork { flex: 1; border: 1px solid var(--frame-line); }
  .artwork-houses {
    background: linear-gradient(180deg, #4a7fb0 0%, #e6c93a 30%, #d63a3a 55%, #5c9a48 75%, #b89aa8 100%);
  }
  .artwork-oldtown {
    background: linear-gradient(180deg, #9fb7c7 0%, #3f7f84 18%, #c8683e 45%, #d9a56a 70%, #4d6f6a 100%);
  }
</style>
</head>
<body>

  <section class="card card-front" aria-label="Business card front">
    <div class="portrait" role="img" aria-label="Portrait photo of Marla Quibbet"></div>
    <div class="accent-block"></div>

    <div class="identity">
      <p class="name">Marla QUIBBET</p>
      <p class="role">Artist of Contemporary</p>
      <p class="role">Modern | Representational Art</p>
    </div>

    <ul class="contacts">
      <li>
        <svg viewBox="0 0 10 10" aria-hidden="true"><rect x="1" y="2.5" width="8" height="5.5"/><path d="M1 2.5 L5 5.8 L9 2.5"/></svg>
        marlaquibbet@fernpost.example
      </li>
      <li>
        <svg viewBox="0 0 10 10" aria-hidden="true"><path d="M2.2 1.2 L3.8 1.2 L4.4 3.2 L3.3 4.1 C3.9 5.4 4.7 6.2 5.9 6.8 L6.8 5.7 L8.8 6.3 L8.8 7.9 C5 8.3 1.7 5 2.2 1.2 Z"/></svg>
        0457219308
      </li>
      <li>
        <svg viewBox="0 0 10 10" aria-hidden="true"><circle cx="5" cy="5" r="4"/><ellipse cx="5" cy="5" rx="1.8" ry="4"/><path d="M1 5 H9"/></svg>
        www.artvault913.com.au/marla-quibbet
      </li>
    </ul>
  </section>

  <section class="card card-back" aria-label="Business card back">
    <div class="artwork artwork-houses" role="img" aria-label="Painting of a row of colourful gabled townhouses reflected in water"></div>
    <div class="artwork artwork-oldtown" role="img" aria-label="Painting of an old town island with church spires and colourful rooftops"></div>
  </section>

</body>
</html>
```